Business Card Design Project

We require business cards to be produced with the following design
http://files.pixelvault-demo.net/img/50329/84172/84172_2093548_50329_image.jpg
Rather than bright meadow, please use Vantelo as the comapny name.
Please also use the following contact details:
1.
Daniel Overbeck
Entrepreneur
07423158871
doverbeck@vantelo-demo.com
2.
Tom Ashworth
Founder
07539402217
tashworth@vantelo-demo.com
Please add:
Facebook favicion facebook.com/vantelo
Linked in favicon linkedin/danieloverbeck
Skype favicon doverbeck
Linked in favicon linkedin/thomasashworth
Skype favicon thomasashworth
Google Plus favicon tomashworth@mailbox-demo.net
To the back

```html
<!DOCTYPE html>
<html lang="en">
<head>
<meta charset="utf-8">
<title>Vantelo — Business Cards</title>
<link rel="stylesheet" href="https://fonts.googleapis.com/css2?family=Questrial&display=swap">
<style>
  :root {
    --stage: #2b2b2b;
    --brand-red: #e30613;
    --ink: #1a1a1a;
    --text-grey: #4a4a4a;
    --rule-grey: #c9c9c9;
    --faint-grey: #ececec;
    --paper: #ffffff;
  }
  * { box-sizing: border-box; margin: 0; padding: 0; }
  html, body {
    width: 1200px; height: 900px; overflow: hidden;
    background: var(--stage);
    font-family: "Questrial", "Century Gothic", sans-serif;
  }
  .stage {
    width: 1200px; height: 900px;
    display: grid;
    grid-template-columns: 560px 560px;
    grid-template-rows: 320px 320px;
    column-gap: 40px; row-gap: 50px;
    align-content: center; justify-content: center;
  }
  .card { position: relative; width: 560px; height: 320px; overflow: hidden; }

  /* Back */
  .card--back { grid-column: 1 / span 2; justify-self: center; background: var(--brand-red); }
  .back__brand {
    position: absolute; left: 50%; top: 50%; transform: translate(-50%, -50%);
    display: flex; flex-direction: column; align-items: flex-start; gap: 8px;
  }
  .back__lockup { display: flex; align-items: center; gap: 16px; color: var(--paper); }
  .back__lockup .brand__mark { width: 52px; height: 52px; background: var(--paper); }
  .back__lockup .brand__name { font-size: 56px; line-height: 1; letter-spacing: -1px; white-space: nowrap; }
  .back__tagline { padding-left: 68px; font-size: 8px; letter-spacing: 0.5px; color: var(--paper); }

  /* Front */
  .card--front { background: var(--paper); }
  .front__decor { position: absolute; left: 0; top: 0; }
  .front__faint-square {
    position: absolute; right: 30px; top: 18px; width: 130px; height: 108px;
    background: var(--faint-grey);
  }
  .front__brand {
    position: absolute; left: 28px; top: 42px;
    display: flex; align-items: center; gap: 12px; color: var(--ink);
  }
  .front__brand .brand__mark { width: 40px; height: 40px; background: var(--brand-red); }
  .front__brand .brand__name { font-size: 42px; line-height: 1; letter-spacing: -1px; }
  .front__tagline {
    position: absolute; left: 30px; top: 94px;
    font-size: 7px; letter-spacing: 0.4px; color: var(--text-grey);
  }
  .person__accent {
    position: absolute; left: 0; top: 178px; width: 10px; height: 46px; background: var(--brand-red);
  }
  .person { position: absolute; left: 28px; top: 176px; }
  .person__name { font-size: 23px; line-height: 1.15; color: var(--text-grey); white-space: nowrap; }
  .person__role { font-size: 17px; line-height: 1.2; color: var(--text-grey); font-style: italic; }

  .contact {
    position: absolute; left: 300px; top: 140px;
    display: flex; gap: 10px;
  }
  .contact__icons, .contact__list { list-style: none; display: flex; flex-direction: column; }
  .contact__icons { width: 16px; align-items: center; }
  .contact__list {
    border-left: 1px solid var(--rule-grey); padding-left: 10px;
    font-size: 13px; color: var(--text-grey);
  }
  .contact__icons li, .contact__list li {
    height: 19px; line-height: 19px; white-space: nowrap;
    display: flex; align-items: center;
  }
  .contact__icons .gap, .contact__list .gap { height: 12px; }
  .social-dot { width: 10px; height: 10px; background: var(--text-grey); }
  .social-dot--round { border-radius: 50%; }
</style>
</head>
<body>
<main class="stage">

  <section class="card card--back" aria-label="Card back">
    <div class="back__brand">
      <div class="back__lockup">
        <span class="brand__mark"></span>
        <span class="brand__name">Vantelo</span>
      </div>
      <p class="back__tagline">A VANTELO COMPANY</p>
    </div>
  </section>

  <section class="card card--front" aria-label="Card front, Daniel Overbeck">
    <svg class="front__decor" width="560" height="320" viewBox="0 0 560 320" aria-hidden="true">
      <polygon points="0,313 235,313 235,320 0,320" fill="#1a1a1a"/>
      <polygon points="235,320 235,302 560,248 560,320" fill="#e30613"/>
    </svg>
    <div class="front__faint-square" aria-hidden="true"></div>
    <div class="front__brand">
      <span class="brand__mark"></span>
      <span class="brand__name">Vantelo</span>
    </div>
    <p class="front__tagline">A VANTELO COMPANY</p>
    <span class="person__accent" aria-hidden="true"></span>
    <div class="person">
      <p class="person__name">Daniel Overbeck</p>
      <p class="person__role">Entrepreneur</p>
    </div>
    <div class="contact">
      <ul class="contact__icons" aria-hidden="true">
        <li><svg width="10" height="15" viewBox="0 0 10 15"><rect x="0.75" y="0.75" width="8.5" height="13.5" rx="1.5" fill="none" stroke="#4a4a4a" stroke-width="1.3"/><line x1="3.5" y1="12" x2="6.5" y2="12" stroke="#4a4a4a" stroke-width="1.2"/></svg></li>
        <li><svg width="15" height="11" viewBox="0 0 15 11"><rect x="0.75" y="0.75" width="13.5" height="9.5" fill="none" stroke="#4a4a4a" stroke-width="1.3"/><polyline points="1,1 7.5,6 14,1" fill="none" stroke="#4a4a4a" stroke-width="1.3"/></svg></li>
        <li class="gap"></li>
        <li><span class="social-dot"></span></li>
        <li><span class="social-dot"></span></li>
        <li><span class="social-dot social-dot--round"></span></li>
      </ul>
      <ul class="contact__list">
        <li>07423158871</li>
        <li>doverbeck@vantelo-demo.com</li>
        <li class="gap"></li>
        <li>vantelo</li>
        <li>danieloverbeck</li>
        <li>doverbeck</li>
      </ul>
    </div>
  </section>

  <section class="card card--front" aria-label="Card front, Tom Ashworth">
    <svg class="front__decor" width="560" height="320" viewBox="0 0 560 320" aria-hidden="true">
      <polygon points="0,313 235,313 235,320 0,320" fill="#1a1a1a"/>
      <polygon points="235,320 235,302 560,248 560,320" fill="#e30613"/>
    </svg>
    <div class="front__faint-square" aria-hidden="true"></div>
    <div class="front__brand">
      <span class="brand__mark"></span>
      <span class="brand__name">Vantelo</span>
    </div>
    <p class="front__tagline">A VANTELO COMPANY</p>
    <span class="person__accent" aria-hidden="true"></span>
    <div class="person">
      <p class="person__name">Tom Ashworth</p>
      <p class="person__role">Founder</p>
    </div>
    <div class="contact">
      <ul class="contact__icons" aria-hidden="true">
        <li><svg width="10" height="15" viewBox="0 0 10 15"><rect x="0.75" y="0.75" width="8.5" height="13.5" rx="1.5" fill="none" stroke="#4a4a4a" stroke-width="1.3"/><line x1="3.5" y1="12" x2="6.5" y2="12" stroke="#4a4a4a" stroke-width="1.2"/></svg></li>
        <li><svg width="15" height="11" viewBox="0 0 15 11"><rect x="0.75" y="0.75" width="13.5" height="9.5" fill="none" stroke="#4a4a4a" stroke-width="1.3"/><polyline points="1,1 7.5,6 14,1" fill="none" stroke="#4a4a4a" stroke-width="1.3"/></svg></li>
        <li class="gap"></li>
        <li><span class="social-dot"></span></li>
        <li><span class="social-dot"></span></li>
        <li><span class="social-dot social-dot--round"></span></li>
      </ul>
      <ul class="contact__list">
        <li>07539402217</li>
        <li>tashworth@vantelo-demo.com</li>
        <li class="gap"></li>
        <li>vantelo</li>
        <li>thomasashworth</li>
        <li>thomasashworth</li>
      </ul>
    </div>
  </section>

</main>
</body>
</html>
```